VELTRA Corp Has New Logo Now Needs New Stationary

We just chose our new logo, and now we need a letterhead and envelope design. I would like both to be used via Microsoft Word so I can print both the letterhead and envelopes myself rather than having to the letterhead and envelopes produced by a printing firm. I has attached the new logo and spec sheet provided by the logo designer.

```html
<!DOCTYPE html>
<html lang="en">
<head>
<meta charset="utf-8">
<title>VELTRA Corp — Envelope Stationery</title>
<link rel="stylesheet" href="https://fonts.googleapis.com/css2?family=Montserrat:wght@700&family=Open+Sans:wght@400&display=swap">
<style>
  :root {
    --bg: #f4f4f4;
    --paper: #ffffff;
    --edge: #e3e3e3;
    --green: #7dc25a;
    --blue: #5db7e4;
    --ink: #2b2b2b;
    --muted: #555555;
    --window: #f1f1f1;
  }
  * { margin: 0; padding: 0; box-sizing: border-box; }
  html, body { width: 1200px; height: 1000px; overflow: hidden; background: var(--bg); }
  .canvas { position: relative; width: 1200px; height: 1000px; }

  .envelope {
    position: absolute;
    left: 160px;
    width: 880px;
    height: 440px;
    background: var(--paper);
    border: 1px solid var(--edge);
    box-shadow: 0 10px 30px rgba(0,0,0,0.08);
  }
  .envelope--back { top: 40px; }
  .envelope--front { top: 520px; }

  .stripe { position: absolute; left: 0; top: 64px; width: 880px; height: 16px; }

  .brand {
    display: flex; align-items: center; gap: 10px;
    font-family: "Montserrat", sans-serif; font-weight: 700;
    color: var(--ink); letter-spacing: 0.5px;
  }
  .brand__dot { width: 16px; height: 16px; border-radius: 50%; background: var(--green); }
  .envelope--back .brand { position: absolute; right: 56px; top: 200px; font-size: 24px; }

  .window {
    position: absolute; left: 560px; top: 90px; width: 270px; height: 150px;
    background: var(--window); border: 1px solid #dcdcdc; border-radius: 4px;
  }

  .sender { position: absolute; left: 56px; top: 250px; }
  .sender .brand { font-size: 22px; }
  .sender__rule { width: 60px; height: 2px; background: var(--green); margin: 10px 0 12px 26px; }
  .contact { list-style: none; font-family: "Open Sans", sans-serif; font-size: 12px; color: var(--muted); }
  .contact li { display: flex; align-items: flex-start; gap: 8px; line-height: 18px; }
  .contact svg { width: 11px; height: 11px; margin-top: 4px; flex: none; fill: var(--blue); }
</style>
</head>
<body>
<main class="canvas">

  <section class="envelope envelope--back" aria-label="Envelope flap side">
    <svg class="stripe" viewBox="0 0 880 16" aria-hidden="true">
      <polygon points="0,0 650,0 640,16 0,16" fill="var(--green)"/>
      <polygon points="666,0 880,0 880,16 656,16" fill="var(--blue)"/>
    </svg>
    <div class="brand"><span class="brand__dot"></span>VELTRA Corp</div>
  </section>

  <section class="envelope envelope--front" aria-label="Envelope address side">
    <div class="window" aria-label="Address window"></div>
    <div class="sender">
      <div class="brand"><span class="brand__dot"></span>VELTRA Corp</div>
      <div class="sender__rule"></div>
      <ul class="contact">
        <li>
          <svg viewBox="0 0 12 12"><path d="M6 0a4 4 0 0 0-4 4c0 3 4 8 4 8s4-5 4-8a4 4 0 0 0-4-4zm0 5.5A1.5 1.5 0 1 1 6 2.5a1.5 1.5 0 0 1 0 3z"/></svg>
          <span>48 Harbor Lane, Westfield,<br>Postal Code, Country</span>
        </li>
        <li>
          <svg viewBox="0 0 12 12"><path d="M3 0l2 3-1.3 1.3a7 7 0 0 0 4 4L9 7l3 2-1 2.5C5 12 0 7 .5 1z"/></svg>
          <span>555-8710-42</span>
        </li>
        <li>
          <svg viewBox="0 0 12 12"><rect x="0" y="1" width="12" height="9" rx="1"/></svg>
          <span>555-8710-42</span>
        </li>
        <li>
          <svg viewBox="0 0 12 12"><path d="M0 2h12v8H0zM1 3l5 3.5L11 3v-.2H1z"/></svg>
          <span>hello@veltramail.com</span>
        </li>
        <li>
          <svg viewBox="0 0 12 12"><circle cx="6" cy="6" r="6"/></svg>
          <span>www.veltracorp.com</span>
        </li>
      </ul>
    </div>
  </section>

</main>
</body>
</html>
```